Hello again,
I am needing to update and adapt a new presentation to the TLR template. This is a remake of our communications presentations.
I can increase the budget again once I have the chance to

Target Market(s)

Our Team Members

Requirements
Must have
• Adhere to the TLR Template
Nice to have
• Some creatifity
Should not have
• Any deviation from our brand design

```html
<!DOCTYPE html>
<html lang="en">
<head>
<meta charset="utf-8">
<title>TLR Communications Deck</title>
<link href="https://fonts.googleapis.com/css2?family=Archivo:wght@400;600;700;800&display=swap" rel="stylesheet">
<style>
:root{
  --bg:#474747;
  --teal:#1b8db0;
  --teal-dark:#0f6f8f;
  --teal-soft:#3aa39b;
  --ink:#222;
  --white:#fff;
  --select:#f06a55;
  --red:#e41c1c;
  --green:#3bd33b;
  --yellow:#f3e51b;
}
*{margin:0;padding:0;box-sizing:border-box}
html,body{width:1200px;height:502px;overflow:hidden;background:var(--bg);font-family:'Archivo',Arial,sans-serif}
.sorter{position:relative;width:1200px;height:502px}
.cell{position:absolute;width:184px}
.slide{position:relative;width:184px;height:103px;background:var(--white);overflow:hidden}
.slide.selected{outline:2px solid var(--select);outline-offset:1px}
.meta{display:flex;justify-content:space-between;align-items:center;margin-top:4px;color:#ddd;font-size:7.5px;font-family:Arial,sans-serif}
.meta svg{width:7px;height:7px}
.brand{position:absolute;font-weight:800;font-size:4.5px;color:var(--ink);letter-spacing:.2px}
.brand.light{color:var(--white)}
.strip{position:absolute;left:0;right:0;bottom:0;height:2px;background:var(--teal)}
.h{position:absolute;font-weight:700;color:var(--teal-soft);line-height:1.1}
.t{position:absolute;font-size:2.6px;color:#555;line-height:1.35}
.photo{position:absolute}
.band{position:absolute;left:0;right:0;background:rgba(27,141,176,.85)}
.band-title{position:absolute;color:var(--white);font-weight:700;font-size:5.5px}
.dot{position:absolute;border-radius:50%;background:var(--teal);color:#fff;font-size:3.4px;font-weight:700;display:flex;align-items:center;justify-content:center;text-align:center;line-height:1}
</style>
</head>
<body>
<div class="sorter">

<!-- Row 1 -->
<div class="cell" style="left:6px;top:5px">
  <div class="slide selected">
    <div class="photo" role="img" aria-label="Restaurant storefront exterior under blue sky" style="inset:0;background:linear-gradient(135deg,#3a86c8,#a33,#c7a27a);clip-path:polygon(78px 0,184px 0,184px 103px,118px 103px)"></div>
    <div class="brand" style="left:7px;top:9px">TLR</div>
    <div class="h" style="left:14px;top:21px;font-size:4.2px;color:var(--teal)">Upcoming Vantage Conversions</div>
    <div class="t" style="left:22px;top:30px;font-size:2.8px;color:var(--teal);font-weight:600;line-height:1.65">• Maple Ridge<br>&nbsp;&nbsp;3/13/22<br>• Red Rock<br>&nbsp;&nbsp;3/14/22<br>• Northgate<br>&nbsp;&nbsp;3/15/22<br>• Citrus Park<br>&nbsp;&nbsp;3/16/22<br>• College Blvd<br>&nbsp;&nbsp;3/16/22<br>• Fish LTO Starts<br>&nbsp;&nbsp;2/23/22<br>• Video Due<br>&nbsp;&nbsp;2/21/22</div>
  </div>
  <div class="meta"><span>1</span><svg viewBox="0 0 10 10"><path d="M5 1l1.2 2.6 2.8.3-2.1 1.9.6 2.8L5 7.2 2.5 8.6l.6-2.8L1 3.9l2.8-.3z" fill="#ddd"/></svg></div>
</div>

<div class="cell" style="left:206px;top:5px">
  <div class="slide">
    <div class="photo" role="img" aria-label="Two people at a construction site" style="inset:0;background:linear-gradient(180deg,#8fb6d6,#a58f72)"></div>
    <div class="band" style="top:68px;bottom:0"></div>
    <div class="band-title" style="left:55px;top:78px">Construction / NRO Updates</div>
    <div class="t" style="left:55px;top:88px;color:#fff">Collecting Bids From<br>Construction Teams</div>
  </div>
  <div class="meta"><span>2</span><svg viewBox="0 0 10 10"><path d="M5 1l1.2 2.6 2.8.3-2.1 1.9.6 2.8L5 7.2 2.5 8.6l.6-2.8L1 3.9l2.8-.3z" fill="#ddd"/></svg></div>
</div>

<div class="cell" style="left:406px;top:5px">
  <div class="slide">
    <div class="brand" style="left:7px;top:9px">TLR</div>
    <div class="h" style="left:17px;top:38px;font-size:8px;color:var(--teal)">What's is your<br>level up?</div>
    <div style="position:absolute;left:92px;top:10px;width:76px;height:86px;border:1px solid #cde;background:#fff">
      <div style="height:46px;background:linear-gradient(#2e8c8a,#1d6f80)"></div>
      <div style="position:absolute;left:22px;top:12px;font-size:6px;font-weight:800;color:#fff">LEVEL UP</div>
      <div class="t" style="left:6px;top:48px;width:64px">Where do you want to be in a year? Set a goal and share it.</div>
      <div class="t" style="left:14px;top:64px;font-weight:700;color:#333">WHAT IS YOUR LEVEL UP?</div>
      <div class="t" style="left:12px;top:70px">New skill? Promotion? A car? A house?</div>
    </div>
    <div class="strip"></div>
  </div>
  <div class="meta"><span>3</span><svg viewBox="0 0 10 10"><path d="M5 1l1.2 2.6 2.8.3-2.1 1.9.6 2.8L5 7.2 2.5 8.6l.6-2.8L1 3.9l2.8-.3z" fill="#ddd"/></svg></div>
</div>

<div class="cell" style="left:606px;top:5px">
  <div class="slide">
    <div class="h" style="left:7px;top:6px;font-size:6px">Meet The Team</div>
    <div class="brand" style="left:168px;top:10px">TLR</div>
    <div style="position:absolute;left:0;top:29px;width:46px;height:66px;background:var(--teal)"></div>
    <div style="position:absolute;left:10px;top:36px;color:#fff;font-weight:700;font-size:6px;line-height:2.4">+14.321<br>+12.173</div>
    <div class="t" style="left:5px;top:64px;width:38px;color:#fff">Together we build a workplace culture that lifts every guest and team member.</div>
    <div class="photo" role="img" aria-label="Headshot of team member" style="left:57px;top:29px;width:20px;height:27px;background:linear-gradient(#5a86a8,#c8a88a)"></div>
    <div class="photo" role="img" aria-label="Headshot of team member" style="left:98px;top:29px;width:20px;height:27px;background:linear-gradient(#d9c3ac,#8a6b55)"></div>
    <div class="photo" role="img" aria-label="Headshot of team member" style="left:140px;top:29px;width:20px;height:27px;background:linear-gradient(#3a5d9c,#c9a082)"></div>
    <div class="t" style="left:55px;top:60px;color:var(--teal);font-weight:700">Evan Marsh</div>
    <div class="t" style="left:96px;top:60px;color:var(--teal);font-weight:700">Lena Brooks</div>
    <div class="t" style="left:140px;top:60px;color:var(--teal);font-weight:700">Owen Clay</div>
    <div class="t" style="left:52px;top:66px;width:30px">CEO. Grew up nearby and started with the group.</div>
    <div class="t" style="left:94px;top:66px;width:30px">Controller. Veteran of finance and accounting.</div>
    <div class="t" style="left:136px;top:66px;width:30px">COO. Sees chances to change lives daily.</div>
    <div class="strip"></div>
  </div>
  <div class="meta"><span>4</span><svg viewBox="0 0 10 10"><path d="M5 1l1.2 2.6 2.8.3-2.1 1.9.6 2.8L5 7.2 2.5 8.6l.6-2.8L1 3.9l2.8-.3z" fill="#ddd"/></svg></div>
</div>

<div class="cell" style="left:806px;top:5px">
  <div class="slide">
    <div class="brand" style="left:7px;top:9px">TLR</div>
    <div class="h" style="left:17px;top:30px;font-size:7.5px;color:var(--teal)">Level Up Counter</div>
    <div class="brand" style="left:45px;top:58px">TLR</div>
    <svg style="position:absolute;left:96px;top:20px" width="80" height="60" viewBox="0 0 80 60">
      <rect x="0" y="0" width="56" height="9" fill="#d6e6a4"/>
      <rect x="0" y="9" width="80" height="12" fill="#2f5e86"/>
      <rect x="0" y="21" width="36" height="38" fill="#9dc6e0"/>
      <g stroke="#555" stroke-width=".3" fill="none">
        <rect x="0" y="0" width="80" height="59"/>
        <path d="M0 4.5h80M0 9h80M0 21h80M0 25.5h80M0 30h80M0 34.5h80M0 39h80M0 43.5h80M0 48h80M0 52.5h80M0 57h80M36 9v50M58 9v50"/>
      </g>
      <g font-size="3" fill="#fff" font-family="Archivo,sans-serif"><text x="12" y="17">Location</text><text x="39" y="15">Current</text><text x="60" y="15">Completed</text></g>
      <g font-size="2.8" fill="#123" font-family="Archivo,sans-serif"><text x="9" y="24.5">College</text><text x="10" y="29">Bayside</text><text x="10" y="33.5">Red Rock</text><text x="9" y="38">Northgate</text><text x="10" y="42.5">Summit</text><text x="8" y="47">Citrus Park</text><text x="9" y="51.5">Maple Rdg</text><text x="7" y="56">Town Center</text></g>
    </svg>
    <div class="strip"></div>
  </div>
  <div class="meta"><span>5</span><svg viewBox="0 0 10 10"><path d="M5 1l1.2 2.6 2.8.3-2.1 1.9.6 2.8L5 7.2 2.5 8.6l.6-2.8L1 3.9l2.8-.3z" fill="#ddd"/></svg></div>
</div>

<div class="cell" style="left:1006px;top:5px">
  <div class="slide">
    <div class="photo" role="img" aria-label="Group of smiling team members in a restaurant" style="inset:0;background:linear-gradient(135deg,#6a2a2a,#c9a58c,#2a2a2a)"></div>
    <div class="band" style="top:72px;bottom:0"></div>
    <div class="band-title" style="left:54px;top:80px">Level Up Achievements</div>
    <div class="t" style="left:54px;top:89px;color:#fff">Marco Vale has successfully completed<br>Barber School</div>
  </div>
  <div class="meta"><span>6</span><svg viewBox="0 0 10 10"><path d="M5 1l1.2 2.6 2.8.3-2.1 1.9.6 2.8L5 7.2 2.5 8.6l.6-2.8L1 3.9l2.8-.3z" fill="#ddd"/></svg></div>
</div>

<!-- Row 2 -->
<div class="cell" style="left:6px;top:131px">
  <div class="slide">
    <div class="photo" role="img" aria-label="Three team members posing in a kitchen" style="inset:0;background:linear-gradient(135deg,#b32626,#5a4a44,#d8d1c8)"></div>
    <div class="band" style="top:68px;bottom:0"></div>
    <div class="band-title" style="left:55px;top:76px">Unique Level Up's</div>
    <div class="t" style="left:55px;top:87px;color:#fff">TLR Family Rivalry:<br>Sam Reed has thrown the gauntlet down and is out to<br>beat fellow Shift Specialist Cole Reed at the Grill!</div>
  </div>
  <div class="meta"><span>7</span><svg viewBox="0 0 10 10"><path d="M5 1l1.2 2.6 2.8.3-2.1 1.9.6 2.8L5 7.2 2.5 8.6l.6-2.8L1 3.9l2.8-.3z" fill="#ddd"/></svg></div>
</div>

<div class="cell" style="left:206px;top:131px">
  <div class="slide">
    <div class="brand" style="left:7px;top:9px">TLR</div>
    <div class="t" style="left:13px;top:35px;width:84px">Great food, awesome fries, and very sweet employees! We come here a couple times a month. The manager should get a raise for how she welcomes everyone. The place is clean, food was fast, and service was attentive and on point. Skip the other burger joints and come here. The manager was very attentive.</div>
    <div class="photo" role="img" aria-label="Mountain road at sunset inside a triangle" style="left:96px;top:9px;width:82px;height:78px;background:linear-gradient(160deg,#3e4f66,#d9a46a,#2b7fa3);clip-path:polygon(62% 0,100% 100%,0 100%)"></div>
    <div class="strip"></div>
  </div>
  <div class="meta"><span>8</span><svg viewBox="0 0 10 10"><path d="M5 1l1.2 2.6 2.8.3-2.1 1.9.6 2.8L5 7.2 2.5 8.6l.6-2.8L1 3.9l2.8-.3z" fill="#ddd"/></svg></div>
</div>

<div class="cell" style="left:406px;top:131px">
  <div class="slide">
    <div class="photo" role="img" aria-label="Commercial restaurant kitchen" style="inset:0;background:linear-gradient(135deg,#8a8a8a,#cfcfcf,#4a4a4a);clip-path:polygon(78px 0,184px 0,184px 103px,118px 103px)"></div>
    <div class="brand" style="left:7px;top:9px">TLR</div>
    <div class="h" style="left:16px;top:40px;font-size:8px">Team member<br>Highlights</div>
    <div class="strip"></div>
  </div>
  <div class="meta"><span>9</span><svg viewBox="0 0 10 10"><path d="M5 1l1.2 2.6 2.8.3-2.1 1.9.6 2.8L5 7.2 2.5 8.6l.6-2.8L1 3.9l2.8-.3z" fill="#ddd"/></svg></div>
</div>

<div class="cell" style="left:606px;top:131px">
  <div class="slide">
    <div class="h" style="left:7px;top:6px;font-size:6px">Global Goal Update</div>
    <div class="brand" style="left:168px;top:10px">TLR</div>
    <div class="photo" role="img" aria-label="Sales goal thermometer poster" style="left:9px;top:21px;width:80px;height:70px;background:linear-gradient(135deg,#fbe3e3,#f6d0d0,#fff)"></div>
    <div class="photo" role="img" aria-label="Period goal thermometer poster" style="left:96px;top:21px;width:80px;height:70px;background:linear-gradient(135deg,#fbe3e3,#f6d0d0,#fff)"></div>
    <div class="strip"></div>
  </div>
  <div class="meta"><span>10</span><svg viewBox="0 0 10 10"><path d="M5 1l1.2 2.6 2.8.3-2.1 1.9.6 2.8L5 7.2 2.5 8.6l.6-2.8L1 3.9l2.8-.3z" fill="#ddd"/></svg></div>
</div>

<div class="cell" style="left:806px;top:131px">
  <div class="slide">
    <div class="h" style="left:7px;top:6px;font-size:6px">TLR Scorecard</div>
    <div class="brand" style="left:168px;top:10px">TLR</div>
    <svg style="position:absolute;left:14px;top:34px" width="158" height="35" viewBox="0 0 158 35">
      <rect width="158" height="35" fill="#fff"/>
      <rect width="158" height="7" fill="#9dc6e0"/>
      <rect x="0" y="7" width="14" height="28" fill="#2f5e86"/>
      <g fill="var(--red)"><rect x="76" y="7" width="8" height="28"/><rect x="100" y="7" width="8" height="28"/><rect x="122" y="7" width="8" height="28"/><rect x="146" y="7" width="12" height="28"/><rect x="52" y="13" width="8" height="22"/><rect x="30" y="16" width="8" height="19"/></g>
      <g fill="var(--green)"><rect x="30" y="7" width="8" height="9"/><rect x="52" y="7" width="8" height="6"/></g>
      <rect x="76" y="7" width="8" height="3" fill="var(--yellow)"/>
      <rect x="30" y="13" width="8" height="3" fill="var(--yellow)"/>
      <g stroke="#333" stroke-width=".25" fill="none"><rect width="158" height="35"/><path d="M0 7h158M0 10.5h158M0 14h158M0 17.5h158M0 21h158M0 24.5h158M0 28h158M0 31.5h158M14 0v35M30 0v35M38 0v35M52 0v35M60 0v35M76 0v35M84 0v35M100 0v35M108 0v35M122 0v35M130 0v35M146 0v35"/></g>
    </svg>
    <div class="strip"></div>
  </div>
  <div class="meta"><span>11</span><svg viewBox="0 0 10 10"><path d="M5 1l1.2 2.6 2.8.3-2.1 1.9.6 2.8L5 7.2 2.5 8.6l.6-2.8L1 3.9l2.8-.3z" fill="#ddd"/></svg></div>
</div>

<div class="cell" style="left:1006px;top:131px">
  <div class="slide">
    <div class="h" style="left:7px;top:6px;font-size:6px">Upcoming Birthdays</div>
    <div class="brand" style="left:168px;top:10px">TLR</div>
    <div class="dot" style="left:20px;top:28px;width:19px;height:19px">Feb<br>22</div>
    <div class="t" style="left:43px;top:34px;font-weight:700;color:#222">Jonas Keller</div><div class="t" style="left:43px;top:38px">Operating Partner</div>
    <div class="dot" style="left:103px;top:28px;width:19px;height:19px">Feb<br>22</div>
    <div class="t" style="left:126px;top:34px;font-weight:700;color:#222">Jonas Keller</div><div class="t" style="left:126px;top:38px">Operating Partner</div>
    <div class="dot" style="left:20px;top:60px;width:19px;height:19px">Feb<br>22</div>
    <div class="t" style="left:43px;top:66px;font-weight:700;color:#222">Jonas Keller</div><div class="t" style="left:43px;top:70px">Operating Partner</div>
    <div class="dot" style="left:104px;top:60px;width:19px;height:19px">Feb<br>22</div>
    <div class="t" style="left:127px;top:66px;font-weight:700;color:#222">Jonas Keller</div><div class="t" style="left:127px;top:70px">Operating Partner</div>
    <div class="strip"></div>
  </div>
  <div class="meta"><span>12</span><svg viewBox="0 0 10 10"><path d="M5 1l1.2 2.6 2.8.3-2.1 1.9.6 2.8L5 7.2 2.5 8.6l.6-2.8L1 3.9l2.8-.3z" fill="#ddd"/></svg></div>
</div>

<!-- Row 3 -->
<div class="cell" style="left:6px;top:257px">
  <div class="slide">
    <div class="h" style="left:9px;top:32px;font-size:6.2px">Welcoming<br>our new<br>Team Members</div>
    <div class="brand" style="left:168px;top:10px">TLR</div>
    <svg style="position:absolute;left:67px;top:10px" width="94" height="88" viewBox="0 0 94 88">
      <rect width="94" height="3" fill="#2f5e86"/>
      <g stroke="#888" stroke-width=".2"><path d="M0 6h94M0 9h94M0 12h94M0 15h94M0 18h94M0 21h94M0 24h94M0 27h94M0 30h94M0 33h94M0 36h94M0 39h94M0 42h94M0 45h94M0 48h94M0 51h94M0 54h94M0 57h94M0 60h94M0 63h94M0 66h94M0 69h94M0 72h94M0 75h94M0 78h94M0 81h94M0 84h94M0 87h94M28 0v87M56 0v87M74 0v87"/></g>
      <g stroke="#9ab" stroke-width="1"><path d="M6 4.5h16M34 7.5h14M60 7.5h10M78 7.5h12M8 10.5h14M34 13.5h16M60 13.5h10M78 13.5h12M6 16.5h16M34 19.5h14M60 19.5h10M78 19.5h12M8 22.5h14M34 25.5h16M60 25.5h10M78 25.5h12M6 28.5h16M34 31.5h14M60 31.5h10M78 31.5h12M8 34.5h14M34 37.5h16M60 37.5h10M78 37.5h12M6 40.5h16M34 43.5h14M60 43.5h10M78 43.5h12M8 46.5h14M34 49.5h16M60 49.5h10M78 49.5h12M6 52.5h16M34 55.5h14M60 55.5h10M78 55.5h12M8 58.5h14M34 61.5h16M60 61.5h10M78 61.5h12M6 64.5h16M34 67.5h14M60 67.5h10M78 67.5h12M8 70.5h14M34 73.5h16M60 73.5h10M78 73.5h12M6 76.5h16M34 79.5h14M60 79.5h10M78 79.5h12M8 82.5h14M34 85.5h16M60 85.5h10M78 85.5h12"/></g>
    </svg>
    <div class="strip"></div>
  </div>
  <div class="meta"><span>13</span><svg viewBox="0 0 10 10"><path d="M5 1l1.2 2.6 2.8.3-2.1 1.9.6 2.8L5 7.2 2.5 8.6l.6-2.8L1 3.9l2.8-.3z" fill="#ddd"/></svg></div>
</div>

<div class="cell" style="left:206px;top:257px">
  <div class="slide">
    <div style="position:absolute;inset:0;background:var(--teal);clip-path:polygon(0 0,53px 0,112px 103px,0 103px)"></div>
    <div style="position:absolute;left:10px;top:19px;width:87px;height:58px;background:#141414;border-radius:2px"></div>
    <div style="position:absolute;left:47px;top:77px;width:12px;height:8px;background:#d8d8d8"></div>
    <div style="position:absolute;left:24px;top:22px;color:#fff;font-size:5.4px">Restaurant Manager</div>
    <div class="photo" role="img" aria-label="Grid of six meme stills" style="left:20px;top:32px;width:68px;height:36px;background:linear-gradient(90deg,#b8643a,#c9c0b8,#a44 60%,#6a8cb0)"></div>
    <div class="h" style="left:109px;top:31px;font-size:8px">Meme <span style="color:var(--teal)">of the<br>week</span></div>
    <div class="brand" style="left:168px;top:10px">TLR</div>
  </div>
  <div class="meta"><span>14</span><svg viewBox="0 0 10 10"><path d="M5 1l1.2 2.6 2.8.3-2.1 1.9.6 2.8L5 7.2 2.5 8.6l.6-2.8L1 3.9l2.8-.3z" fill="#ddd"/></svg></div>
</div>

<div class="cell" style="left:406px;top:257px">
  <div class="slide">
    <div class="photo" role="img" aria-label="Black and white mountain range and open road" style="inset:0;background:linear-gradient(180deg,#b8b8b8,#5a5a5a 35%,#fff 35%,#fff 68%,#6a6a6a 68%,#aaa)"></div>
    <div style="position:absolute;left:0;right:0;top:68px;height:2px;background:var(--teal)"></div>
    <div class="brand" style="left:18px;top:53px;font-size:7px">TLR</div>
    <div style="position:absolute;left:47px;top:43px;width:.6px;height:17px;background:#999"></div>
    <div class="h" style="left:54px;top:47px;font-size:8.5px;color:var(--teal)">QUOTE OF THE WEEK</div>
  </div>
  <div class="meta"><span>15</span><svg viewBox="0 0 10 10"><path d="M5 1l1.2 2.6 2.8.3-2.1 1.9.6 2.8L5 7.2 2.5 8.6l.6-2.8L1 3.9l2.8-.3z" fill="#ddd"/></svg></div>
</div>

<div class="cell" style="left:606px;top:257px">
  <div class="slide">
    <div class="photo" role="img" aria-label="Stacked hands of a team" style="inset:0;background:linear-gradient(135deg,#5b463c,#a58a79,#3c3c3c)"></div>
    <div style="position:absolute;left:18px;top:15px;width:148px;height:75px;background:rgba(20,140,180,.9)"></div>
    <div class="brand light" style="left:86px;top:30px">TLR</div>
    <div class="band-title" style="left:62px;top:53px;font-size:7px">Hero Fund</div>
    <div class="t" style="left:70px;top:65px;color:#fff">- Just and example when needed -</div>
  </div>
  <div class="meta"><span>16</span><svg viewBox="0 0 10 10"><path d="M5 1l1.2 2.6 2.8.3-2.1 1.9.6 2.8L5 7.2 2.5 8.6l.6-2.8L1 3.9l2.8-.3z" fill="#ddd"/></svg></div>
</div>

<div class="cell" style="left:806px;top:257px">
  <div class="slide" style="background:var(--teal)">
    <div class="photo" role="img" aria-label="Colorful decorated cookies at a market" style="inset:0;background:linear-gradient(135deg,#e0412f,#f2b84a,#c0396b);clip-path:polygon(184px 0,184px 103px,44px 103px)"></div>
    <div class="brand light" style="left:9px;top:16px">TLR</div>
    <div class="h" style="left:9px;top:27px;font-size:8px;color:#fff">Local Store<br>Marketing</div>
    <div class="t" style="left:9px;top:50px;color:#fff">Custard Cookie Drop offs for Graduating<br>Seniors of 2022</div>
  </div>
  <div class="meta"><span>17</span><svg viewBox="0 0 10 10"><path d="M5 1l1.2 2.6 2.8.3-2.1 1.9.6 2.8L5 7.2 2.5 8.6l.6-2.8L1 3.9l2.8-.3z" fill="#ddd"/></svg></div>
</div>

<div class="cell" style="left:1006px;top:257px">
  <div class="slide" style="background:#000">
    <div class="photo" role="img" aria-label="Studio microphone tinted teal" style="left:0;top:0;width:72px;height:103px;background:linear-gradient(135deg,#0d4f6a,#2a8fb0,#0a3b52)"></div>
    <div class="band-title" style="left:90px;top:10px;font-size:8px">Voice of the Guest</div>
    <svg style="position:absolute;left:78px;top:34px" width="102" height="50" viewBox="0 0 102 50">
      <rect y="4" width="102" height="3" fill="#1b64c0"/>
      <g fill="var(--red)"><rect x="64" y="8" width="12" height="3"/><rect x="64" y="38" width="12" height="3"/></g>
      <g fill="#ccc"><rect x="0" y="8.5" width="30" height="1"/><rect x="0" y="12.5" width="26" height="1"/><rect x="0" y="16.5" width="28" height="1"/><rect x="0" y="20.5" width="22" height="1"/><rect x="0" y="24.5" width="30" height="1"/><rect x="0" y="28.5" width="28" height="1"/><rect x="0" y="32.5" width="20" height="1"/><rect x="0" y="36.5" width="34" height="1"/><rect x="0" y="40.5" width="8" height="1"/></g>
      <g fill="#ddd"><rect x="42" y="8.5" width="5" height="1"/><rect x="52" y="8.5" width="5" height="1"/><rect x="82" y="8.5" width="5" height="1"/><rect x="92" y="8.5" width="5" height="1"/><rect x="42" y="16.5" width="5" height="1"/><rect x="52" y="16.5" width="5" height="1"/><rect x="68" y="16.5" width="5" height="1"/><rect x="92" y="16.5" width="5" height="1"/><rect x="42" y="24.5" width="5" height="1"/><rect x="52" y="24.5" width="5" height="1"/><rect x="68" y="24.5" width="5" height="1"/><rect x="92" y="24.5" width="5" height="1"/><rect x="42" y="32.5" width="5" height="1"/><rect x="68" y="32.5" width="5" height="1"/><rect x="92" y="32.5" width="5" height="1"/><rect x="42" y="44.5" width="5" height="1"/><rect x="68" y="44.5" width="5" height="1"/><rect x="92" y="44.5" width="5" height="1"/></g>
    </svg>
  </div>
  <div class="meta"><span>18</span><svg viewBox="0 0 10 10"><path d="M5 1l1.2 2.6 2.8.3-2.1 1.9.6 2.8L5 7.2 2.5 8.6l.6-2.8L1 3.9l2.8-.3z" fill="#ddd"/></svg></div>
</div>

<!-- Row 4 -->
<div class="cell" style="left:6px;top:383px">
  <div class="slide">
    <div class="photo" role="img" aria-label="Hand holding a gold medal, teal tint" style="left:0;right:0;top:0;height:61px;background:linear-gradient(135deg,#1c7fa2,#4ba9c6,#1d6e8c)"></div>
    <div style="position:absolute;left:0;right:0;top:61px;height:2px;background:var(--teal)"></div>
    <div class="brand" style="left:18px;top:80px;font-size:7px">TLR</div>
    <div style="position:absolute;left:46px;top:70px;width:.6px;height:20px;background:#999"></div>
    <div class="h" style="left:53px;top:77px;font-size:7.6px;color:var(--teal)">TEAM MEMBER <span style="color:var(--teal-soft)">OF THE PERIOD</span></div>
    <div class="strip"></div>
  </div>
  <div class="meta"><span>19</span><svg viewBox="0 0 10 10"><path d="M5 1l1.2 2.6 2.8.3-2.1 1.9.6 2.8L5 7.2 2.5 8.6l.6-2.8L1 3.9l2.8-.3z" fill="#ddd"/></svg></div>
</div>

<div class="cell" style="left:206px;top:383px">
  <div class="slide">
    <div class="photo" role="img" aria-label="Portrait of the team member of the period" style="inset:0;background:linear-gradient(135deg,#c89a7a,#7a4a34,#d8b8a0);clip-path:polygon(78px 0,184px 0,184px 103px,118px 103px)"></div>
    <div class="brand" style="left:7px;top:9px">TLR</div>
    <div class="h" style="left:16px;top:40px;font-size:7.8px">Team Member:<br>Nora Ellis</div>
    <div class="t" style="left:18px;top:64px;width:52px;color:#333">They are an extremely adept team member and they've been a gigantic help with covering shifts and helping train up new members of our team</div>
    <div class="strip"></div>
  </div>
  <div class="meta"><span>20</span><svg viewBox="0 0 10 10"><path d="M5 1l1.2 2.6 2.8.3-2.1 1.9.6 2.8L5 7.2 2.5 8.6l.6-2.8L1 3.9l2.8-.3z" fill="#ddd"/></svg></div>
</div>

<div class="cell" style="left:406px;top:383px">
  <div class="slide">
    <div class="h" style="left:7px;top:6px;font-size:6px">Quarterly Focus</div>
    <div class="brand" style="left:168px;top:10px">TLR</div>
    <div class="photo" role="img" aria-label="Abstract teal light tunnel" style="left:0;right:0;top:22px;height:40px;background:radial-gradient(circle at 50% 50%,#bfe9f0,#2a9bb5 40%,#0f4d60)"></div>
    <svg style="position:absolute;left:10px;top:68px" width="168" height="12" viewBox="0 0 168 12" fill="none" stroke="var(--teal)" stroke-width=".7">
      <circle cx="8" cy="6" r="3.5"/><path d="M6.5 6l1.2 1.2 2-2.4"/>
      <rect x="33" y="2.5" width="8" height="7"/><path d="M33 5h8"/>
      <path d="M62 4l3 3 3-3 3 3 3-3"/>
      <path d="M92 4a3 3 0 016 0c0 3-6 6-6 6s-6-3-6-6a3 3 0 016 0"/>
      <path d="M121 4l3 3 3-3 3 3 3-3"/>
      <path d="M152 4a3 3 0 016 0c0 3-6 6-6 6s-6-3-6-6a3 3 0 016 0"/>
    </svg>
    <div class="t" style="left:6px;top:81px;width:170px;display:flex;justify-content:space-between;text-align:center;color:#333">
      <span>Flawless 4 Wall<br>Execution</span><span>Local Store<br>Marketing</span><span>Sunburger<br>Opening in Co</span><span>Fish &amp; Mint<br>Cocoa Concrete</span><span>Sunburger<br>Opening in Co</span><span>Fish &amp; Mint Cocoa<br>Concrete / Cookie</span>
    </div>
    <div class="strip"></div>
  </div>
  <div class="meta"><span>21</span><svg viewBox="0 0 10 10"><path d="M5 1l1.2 2.6 2.8.3-2.1 1.9.6 2.8L5 7.2 2.5 8.6l.6-2.8L1 3.9l2.8-.3z" fill="#ddd"/></svg></div>
</div>

<div class="cell" style="left:606px;top:383px">
  <div class="slide">
    <div class="brand" style="left:7px;top:9px">TLR</div>
    <div class="h" style="left:12px;top:28px;font-size:8px">Year to date<br>Promotions</div>
    <div class="t" style="left:13px;top:53px;color:var(--red);font-weight:700;line-height:1.5">• Jonas Keller<br><span style="color:#555;font-weight:400">&nbsp;&nbsp;Operating Partner</span><br><br>• Mia Lorne<br><span style="color:#555;font-weight:400">&nbsp;&nbsp;Operating Partner</span><br><br>• Marco Vale<br><span style="color:#555;font-weight:400">&nbsp;&nbsp;Operating Partner</span></div>
    <div class="photo" role="img" aria-label="Career growth mountain illustration with milestone path" style="left:88px;top:0;width:96px;height:103px;background:linear-gradient(180deg,#e8edf0 20%,#3f8ea0 50%,#1f5f70)"></div>
    <div style="position:absolute;left:95px;top:4px;color:#333;font-size:8px">CAREER</div>
    <div style="position:absolute;left:96px;top:14px;color:var(--red);font-size:3px;font-weight:700">GROWTH WITH US</div>
  </div>
  <div class="meta"><span>22</span><svg viewBox="0 0 10 10"><path d="M5 1l1.2 2.6 2.8.3-2.1 1.9.6 2.8L5 7.2 2.5 8.6l.6-2.8L1 3.9l2.8-.3z" fill="#ddd"/></svg></div>
</div>

<div class="cell" style="left:806px;top:383px">
  <div class="slide" style="background:var(--teal)">
    <div class="brand light" style="left:82px;top:46px;font-size:8px">TLR</div>
  </div>
  <div class="meta"><span>23</span><svg viewBox="0 0 10 10"><path d="M5 1l1.2 2.6 2.8.3-2.1 1.9.6 2.8L5 7.2 2.5 8.6l.6-2.8L1 3.9l2.8-.3z" fill="#ddd"/></svg></div>
</div>

</div>
</body>
</html>
```